Business Card Design for Mortgage Broking Business

We need to redesign the business card. Mortgage broking business, doing home loan and commercial loans, existing logo, also RQTB member logo. design style needs to be simple, professional, elegant.

once final, need to setup for a team of different names and contact details.

Industry/Entity Type

Loan

Contact Information for Business Card

Name; Mobile; Email; Address; Tel; Fax; Australian Credit Licence: 618204

```html
<!DOCTYPE html>
<html lang="en">
<head>
<meta charset="utf-8">
<title>Harbourline Lending – Business Card</title>
<link rel="stylesheet" href="https://fonts.googleapis.com/css2?family=Libre+Baskerville:wght@700&family=Roboto:wght@500;700&display=swap">
<style>
  :root {
    --bg: #e4e5ea;
    --card: #ffffff;
    --navy: #2e3192;
    --indigo: #5b5fa8;
    --green: #3aa655;
    --teal: #2596c9;
    --ink: #222222;
    --grey: #5a5a5a;
  }
  * { margin: 0; padding: 0; box-sizing: border-box; }
  html, body { width: 1200px; height: 871px; overflow: hidden; }
  body {
    background: var(--bg);
    position: relative;
    font-family: "Roboto", Arial, sans-serif;
  }
  .card {
    position: absolute;
    left: 240px;
    width: 720px;
    height: 411px;
    background: var(--card);
    box-shadow: 0 4px 18px rgba(0,0,0,0.12);
    overflow: hidden;
  }
  .card--front { top: 14px; }
  .card--back { top: 446px; }

  /* brand name (plain wordmark) */
  .brand {
    position: absolute;
    display: flex;
    align-items: center;
    font-family: "Libre Baskerville", Georgia, serif;
    font-weight: 700;
    color: var(--indigo);
    white-space: nowrap;
  }
  .brand__square { background: var(--green); flex: none; }

  /* front */
  .card--front .brand {
    left: 0; right: 0; top: 110px;
    justify-content: center; gap: 14px; font-size: 40px;
  }
  .card--front .brand__square { width: 30px; height: 30px; }
  .services {
    position: absolute; left: 0; right: 0; top: 198px;
    text-align: center;
    font-weight: 700; font-size: 25px; letter-spacing: 0.5px;
    color: var(--grey);
  }
  .website {
    position: absolute; left: 0; right: 0; top: 240px;
    text-align: center;
    font-weight: 700; font-size: 25px; letter-spacing: 0.5px;
    color: var(--grey);
  }
  .website__tld { color: var(--navy); }

  .band { position: absolute; height: 14px; }
  .card--front .band--green { left: 0; width: 190px; bottom: 0; background: var(--green); }
  .card--front .band--navy  { left: 208px; width: 330px; bottom: 0; background: var(--navy); }
  .card--front .band--teal  { left: 556px; width: 164px; bottom: 0; background: var(--teal); }

  /* back */
  .card--back .brand {
    left: 40px; top: 152px;
    gap: 12px; font-size: 22px;
  }
  .card--back .brand__square { width: 24px; height: 24px; }
  .divider {
    position: absolute; left: 362px; top: 92px;
    width: 3px; height: 152px; background: var(--navy);
  }
  .contact { position: absolute; left: 388px; top: 100px; }
  .contact__name {
    font-family: "Libre Baskerville", Georgia, serif;
    font-weight: 700; font-size: 30px; color: var(--ink);
    margin-bottom: 14px; letter-spacing: 0.5px;
    white-space: nowrap;
  }
  .contact__row {
    display: flex; align-items: center; gap: 9px;
    font-weight: 700; font-size: 15px; color: var(--ink);
    letter-spacing: 0.2px; margin-bottom: 9px;
    white-space: nowrap;
  }
  .contact__icon { width: 14px; height: 14px; flex: none; fill: var(--navy); }

  .card--back .band--navy  { left: 0; width: 440px; bottom: 54px; background: var(--navy); }
  .card--back .band--green { left: 658px; width: 62px; bottom: 54px; background: var(--green); }
  .member-badge {
    position: absolute; left: 478px; bottom: 34px;
    width: 160px; height: 52px;
    border: 4px solid var(--navy);
    background: #f4f7f4;
  }
</style>
</head>
<body>

  <section class="card card--front" aria-label="Business card front">
    <div class="brand"><span class="brand__square"></span>Harbourline Lending</div>
    <p class="services">Home Loan | Commercial Loan</p>
    <p class="website">yourwebsite<span class="website__tld">.com</span></p>
    <span class="band band--green"></span>
    <span class="band band--navy"></span>
    <span class="band band--teal"></span>
  </section>

  <section class="card card--back" aria-label="Business card back">
    <div class="brand"><span class="brand__square"></span>Harbourline Lending</div>
    <span class="divider"></span>
    <div class="contact">
      <h1 class="contact__name">Your Name</h1>
      <p class="contact__row">
        <svg class="contact__icon" viewBox="0 0 16 16" aria-hidden="true"><path d="M8 0a5.5 5.5 0 0 0-5.5 5.5C2.5 10 8 16 8 16s5.5-6 5.5-10.5A5.5 5.5 0 0 0 8 0zm0 7.8a2.3 2.3 0 1 1 0-4.6 2.3 2.3 0 0 1 0 4.6z"/></svg>
        1212 somewhere, Anywhere , Anywhere
      </p>
      <p class="contact__row">
        <svg class="contact__icon" viewBox="0 0 16 16" aria-hidden="true"><path d="M1 5c0-2 3-3 7-3s7 1 7 3v1.5h-3.5V5h-7v1.5H1zM3.5 7.5h9l1.5 6.5H2z"/></svg>
        000-000-000
      </p>
      <p class="contact__row">
        <svg class="contact__icon" viewBox="0 0 16 16" aria-hidden="true"><path d="M1 3h14v10H1zm1.5 1.5v.4L8 9l5.5-4.1v-.4z"/></svg>
        Email@
      </p>
    </div>
    <span class="band band--navy"></span>
    <span class="member-badge" role="img" aria-label="Member accreditation badge"></span>
    <span class="band band--green"></span>
  </section>

</body>
</html>
```